Manuka Honey company needs a Upmarket, Luxury Website!

New Zealand, Taranaki based Manuka Honey company Marumaru Honey is looking for a new website, we are looking for an upmarket, luxury, serious website design. We export the highest quality quality Manuka Honey, straight from the Taranaki region.

Main export markets are Asia & Europe, also New Zealand & Australia.

Looking to have a beautiful, upmarket, serious, luxurious & graphical experience with mobile optimization in mind. Like the use of product staging/mockups

You can use copy from other websites to build the site and we will change the copy after the design is finished.

***Please include 'Honey Product' mockups in website.

*Will add illustrator files in coming days***

Feel free to make website functional in Shopify, Wordpress or WIX

Target Market(s)

Asia, Europe (main markets) New Zealand, Australia (Submarkets)

Coding

Coded - Design and coding required

Number of Pages Required

4 page

Requirements
Must have
• Home, Shop, About Us, Contact Us

Homepage to include:

Our Products
Company Video (video under construction)
What is MGO/UMF
Newsletter Opt-in

***(Not in Order)***

Please include 'Honey Product' mockups in website.
*Will add illustrator files in coming days
Nice to have
• FAQ & Partnership Inquiries (hyperlink in footer)

```html
<!DOCTYPE html>
<html lang="en">
<head>
<meta charset="utf-8">
<title>Marumaru Honey — Manuka Honey from Taranaki</title>
<link href="https://fonts.googleapis.com/css2?family=Poppins:wght@400;500;600;700&display=swap" rel="stylesheet">
<style>
:root{
  --ink:#1f1f1f;
  --dark:#222222;
  --gold:#c9a54f;
  --gold-light:#e3c774;
  --gold-pale:#f5ea9c;
  --text:#333333;
  --muted:#555555;
  --white:#ffffff;
}
*{box-sizing:border-box;margin:0;padding:0}
html,body{width:1200px;height:4498px;overflow:hidden}
body{position:relative;font-family:'Poppins',sans-serif;color:var(--text);background:var(--white)}
.abs{position:absolute}
.btn{position:absolute;display:flex;align-items:center;justify-content:center;background:linear-gradient(90deg,var(--gold-pale),var(--gold));color:var(--ink);font-weight:700;font-size:14px;letter-spacing:.5px}

/* hero */
.hero-panel{left:0;top:0;width:629px;height:751px;background:var(--dark)}
.brand{left:87px;top:17px;width:300px;height:117px;display:flex;align-items:center;gap:14px;color:var(--gold);font-weight:600;font-size:22px}
.brand-dot{width:40px;height:40px;border:2px solid var(--gold);border-radius:50%}
.nav{left:629px;top:0;width:571px;height:68px;background:var(--white);display:flex;align-items:center;padding-left:58px;gap:34px;font-size:13px;font-weight:500;color:var(--ink)}
.nav .active{color:var(--gold)}
.nav-icons{display:flex;gap:12px;margin-left:-8px}
.hero-photo{left:568px;top:68px;width:632px;height:634px;background:linear-gradient(170deg,#9aa7a5 0%,#8b8a70 40%,#5c6a46 70%,#6f6a5c 100%)}
.hero-title{left:89px;top:326px;font-weight:700;font-size:50px;line-height:46px;color:var(--white)}
.hero-title span{color:var(--gold)}
.hero-sub{left:89px;top:428px;width:420px;font-size:15px;line-height:19px;color:#e6e6e6}

/* about */
.about-pattern{left:0;top:816px;width:372px;height:581px;background:#ececec}
.about-photo{left:87px;top:873px;width:454px;height:454px;background:linear-gradient(180deg,#7d99c0 0%,#c9d6e6 35%,#4d6a3a 60%,#5c7e3a 100%);box-shadow:20px 30px 40px rgba(0,0,0,.12)}
.h2{font-weight:700;font-size:40px;color:var(--ink);letter-spacing:.5px}
.h2 span{color:var(--gold-light)}
.rule{width:52px;height:3px;background:var(--gold)}
.body-copy{font-size:15px;line-height:24px;color:var(--text)}

/* products */
.products{left:0;top:1441px;width:1200px;height:589px;background:linear-gradient(90deg,#f7ee9f 0%,#efdc8b 50%,#c9a55a 100%)}
.products-title{left:0;top:1538px;width:1200px;text-align:center;font-weight:600;font-size:42px;color:var(--ink)}
.card{position:absolute;top:1677px;width:246px;height:271px;background:var(--white);text-align:center}
.jar{position:absolute;left:50px;top:-35px;width:146px;height:176px;border-radius:10px 10px 14px 14px}
.jar::before{content:"";position:absolute;left:0;top:0;width:100%;height:34px;background:#1b1b1b;border-radius:8px 8px 0 0}
.card h3{position:absolute;left:0;top:180px;width:100%;font-size:15px;font-weight:600;color:var(--ink)}
.stars{position:absolute;left:0;top:204px;width:100%;font-size:13px;letter-spacing:3px;color:var(--gold-light)}
.price{position:absolute;left:0;top:222px;width:100%;font-size:20px;font-weight:600;color:var(--gold)}

/* mgo */
.mgo-photo{left:658px;top:2030px;width:542px;height:569px;background:radial-gradient(circle at 55% 60%,#c7822a 0%,#8a5a22 25%,#2b2b2b 55%,#1c1c1c 100%)}
.mgo-list{left:89px;top:2355px;font-size:15px;line-height:27px;color:var(--text)}

/* video */
.video{left:89px;top:2688px;width:1022px;height:488px;background:linear-gradient(100deg,#3d78b3 0%,#8cb4d4 35%,#c48a2e 55%,#3b4f6a 100%)}
.play{left:213px;top:2919px;width:84px;height:84px;border:3px solid var(--white);border-radius:50%}
.video-title{left:641px;top:2915px;font-size:40px;line-height:44px;font-weight:500;color:var(--white)}

/* review */
.quote{left:0;top:3240px;width:1200px;text-align:center;font-size:150px;line-height:150px;font-weight:700;color:#efefef}
.review-title{left:0;top:3310px;width:1200px;text-align:center;font-size:42px;font-weight:500;color:var(--ink)}
.review-title span{color:var(--gold-light)}
.review-copy{left:270px;top:3393px;width:660px;text-align:center;font-size:15px;line-height:23px;color:var(--text)}
.reviewer{left:0;top:3472px;width:1200px;text-align:center;font-size:15px;font-weight:600;color:var(--ink)}
.role{left:0;top:3496px;width:1200px;text-align:center;font-size:13px;color:var(--muted)}
.dots{left:582px;top:3536px;display:flex;gap:5px}
.dots i{width:8px;height:8px;border-radius:50%;background:#bbb}
.dots i:first-child{background:var(--gold)}

/* partner + newsletter */
.partner{left:0;top:3625px;width:1200px;height:436px;background:linear-gradient(90deg,#2a2a2a,#1e1e1e)}
.partner-photo{left:0;top:3625px;width:530px;height:340px;background:radial-gradient(circle at 75% 75%,#d9932a 0%,#a86f2a 25%,rgba(42,42,42,0) 55%)}
.partner-small{left:582px;top:3762px;font-size:27px;font-weight:600;line-height:30px;color:var(--white)}
.partner-small b{display:block;font-size:22px;font-weight:600}
.partner-big{left:718px;top:3790px;font-size:58px;font-weight:700;color:var(--gold-light)}
.newsletter{left:87px;top:3965px;width:1024px;height:161px;background:linear-gradient(90deg,#f6ec9d,#c9a354)}
.news-title{left:154px;top:4018px;font-size:36px;line-height:38px;font-weight:700;color:var(--ink)}
.news-input{left:587px;top:4026px;width:386px;height:44px;background:var(--white);font-size:13px;color:#555;display:flex;align-items:center;padding-left:22px}
.news-btn{left:973px;top:4026px;width:138px;height:44px;background:var(--ink);color:var(--white);font-size:13px;font-weight:600;display:flex;align-items:center;justify-content:center}

/* footer */
.footer{left:0;top:4061px;width:1200px;height:437px;background:var(--dark)}
.footer-brand{left:105px;top:4236px;width:200px;height:140px;display:flex;flex-direction:column;align-items:center;justify-content:center;gap:10px;color:var(--gold);font-size:20px;font-weight:600}
.footer-brand .brand-dot{width:46px;height:46px}
.fcol{position:absolute;top:4248px}
.fcol h4{font-size:18px;font-weight:600;color:var(--gold);margin-bottom:8px}
.fcol a{display:block;font-size:14px;line-height:29px;color:#cfcfcf;text-decoration:none}
.social{position:absolute;top:4292px;width:32px;height:32px;border:1px solid #666;border-radius:50%}
.copyright{left:0;top:4464px;width:1200px;text-align:center;font-size:13px;color:var(--gold)}
.top-btn{left:1128px;top:4429px;width:32px;height:32px;border-radius:50%;background:var(--gold);display:flex;align-items:center;justify-content:center}
</style>
</head>
<body>

<div class="abs hero-panel"></div>
<div class="abs brand"><span class="brand-dot"></span>Marumaru Honey</div>
<nav class="abs nav">
  <span class="active">HOME</span><span>SHOP</span><span>ABOUT US</span><span>CONTACT US</span>
  <span class="nav-icons">
    <svg width="18" height="18" viewBox="0 0 18 18" fill="none" stroke="#1f1f1f" stroke-width="2"><circle cx="7.5" cy="7.5" r="5.5"/><path d="M12 12l5 5"/></svg>
    <svg width="18" height="18" viewBox="0 0 18 18" fill="none" stroke="#1f1f1f" stroke-width="1.6"><circle cx="9" cy="6" r="4"/><path d="M2 17c1-4 4-6 7-6s6 2 7 6"/></svg>
    <svg width="22" height="20" viewBox="0 0 22 20" fill="none" stroke="#1f1f1f" stroke-width="1.6"><path d="M2 7h14l-1 11H3z"/><path d="M6 7V5a3 3 0 0 1 6 0v2"/><circle cx="18" cy="4" r="4" fill="#c9a54f" stroke="none"/></svg>
  </span>
</nav>
<div class="abs hero-photo" role="img" aria-label="Beekeepers in protective suits walking in front of a hillside apiary"></div>
<h1 class="abs hero-title">WELCOME<br><span>MARUMARU HONEY</span></h1>
<p class="abs hero-sub">We export the highest quality quality Manuka Honey, straight from the Taranaki region.</p>
<a class="btn" style="left:89px;top:484px;width:129px;height:31px">SHOP NOW</a>

<div class="abs about-pattern" role="img" aria-label="Light grey decorative swirl pattern"></div>
<div class="abs about-photo" role="img" aria-label="Beekeepers tending hives in a green valley under a bright sky"></div>
<h2 class="abs h2" style="left:601px;top:992px">ABOUT <span>US</span></h2>
<div class="abs rule" style="left:601px;top:1052px"></div>
<p class="abs body-copy" style="left:601px;top:1068px;width:520px">Lorem Ipsum is simply dummy text of the printing and typesetting industry. Lorem Ipsum has been the industry's standard dummy text ever since the 1500s, when an unknown printer took a galley of type and scrambled it to make a type specimen book. It has survived not only five centuries, but also the leap into electronic typesetting, remaining essentially unchanged.</p>
<a class="btn" style="left:601px;top:1228px;width:115px;height:31px;font-size:13px">READ MORE</a>

<section class="abs products"></section>
<h2 class="abs products-title">OUR PRODUCTS</h2>
<div class="card" style="left:89px"><div class="jar" role="img" aria-label="Manuka honey jar with purple label" style="background:#5a2d7d"></div><h3>Products Heading here</h3><div class="stars">★★★★★</div><div class="price">$25.00</div></div>
<div class="card" style="left:347px"><div class="jar" role="img" aria-label="Manuka honey jar with blue label" style="background:#1d3f86"></div><h3>Products Heading here</h3><div class="stars">★★★★★</div><div class="price">$25.00</div></div>
<div class="card" style="left:606px"><div class="jar" role="img" aria-label="Manuka honey jar with orange-red label" style="background:#b04a26"></div><h3>Products Heading here</h3><div class="stars">★★★★★</div><div class="price">$25.00</div></div>
<div class="card" style="left:863px"><div class="jar" role="img" aria-label="Manuka honey jar with green label" style="background:#2f7a3c"></div><h3>Products Heading here</h3><div class="stars">★★★★★</div><div class="price">$25.00</div></div>

<h2 class="abs h2" style="left:89px;top:2178px;font-weight:500">WHAT IS <span>MGO/UMF</span></h2>
<div class="abs rule" style="left:89px;top:2234px"></div>
<p class="abs body-copy" style="left:89px;top:2250px;width:520px">Lorem Ipsum is simply dummy text of the printing and typesetting industry. Lorem Ipsum has been the industry's standard dummy text ever since the 1500s, when an unknown printer took a galley of type and scrambled it to make a type specimen book.</p>
<div class="abs mgo-list">UMF 5 = MGO83<br>UMF10 = MGO263<br>UMF15 = MGO514<br>UMF20 = MGO829<br>UMF25 = MGO1200</div>
<a class="btn" style="left:89px;top:2498px;width:115px;height:31px;font-size:13px">READ MORE</a>
<div class="abs mgo-photo" role="img" aria-label="Jars of honey with a wooden dipper and honeycomb on a dark surface"></div>

<div class="abs video" role="img" aria-label="Beekeeper holding a honeycomb frame surrounded by bees"></div>
<div class="abs play"><svg width="78" height="78" viewBox="0 0 78 78"><path d="M31 25l22 14-22 14z" fill="#fff"/></svg></div>
<h2 class="abs video-title">UNLOCKING<br>NATURE'S SECRETS</h2>

<div class="abs quote">“</div>
<h2 class="abs review-title">CUSTOMER <span>REVIEW</span></h2>
<p class="abs review-copy">Lorem Ipsum is simply dummy text of the printing and typesetting industry.Lorem Ipsum has been the industry's standard dummy text ever since the when an unknown printer .</p>
<div class="abs reviewer">JOHN SMITH</div>
<div class="abs role">Co founder</div>
<div class="abs dots"><i></i><i></i><i></i></div>

<section class="abs partner"></section>
<div class="abs partner-photo" role="img" aria-label="Hand holding a dripping piece of honeycomb"></div>
<div class="abs partner-small">THESE ARE OUR<b>RESPECTED</b></div>
<div class="abs partner-big">PARTNER</div>

<section class="abs footer"></section>
<div class="abs newsletter"></div>
<h2 class="abs news-title">SUBSCRIBE TO<br>OUR NEWSLETTER</h2>
<div class="abs news-input">Enter your email</div>
<div class="abs news-btn">SUBSCRIBE</div>

<div class="abs footer-brand"><span class="brand-dot"></span>Marumaru Honey</div>
<div class="fcol" style="left:328px"><h4>WHO WE ARE</h4><a>About Us</a><a>FAQ</a><a>Partnership Inquiries</a></div>
<div class="fcol" style="left:564px"><h4>LET US HELP</h4><a>Shipping</a><a>FAQ</a><a>My Account</a></div>
<div class="fcol" style="left:753px"><h4>EXPLORE</h4><a>Ingredients</a><a>Blog</a><a>Privacy Policy</a></div>
<span class="social" style="left:939px"></span>
<span class="social" style="left:982px"></span>
<span class="social" style="left:1023px"></span>
<span class="social" style="left:1065px"></span>
<div class="abs copyright">Copyright 2021 | All Rights Reserved</div>
<div class="abs top-btn"><svg width="12" height="8" viewBox="0 0 12 8" fill="none" stroke="#1f1f1f" stroke-width="2"><path d="M1 7l5-5 5 5"/></svg></div>

</body>
</html>
```